Business card for a gourmet fruit and vegetable retail store

Please design a business card for our boutique gourmet fruit and vegetable food store using attached logo design, with the colour options of white, black and lime green. We would like it to be unique and classic, with a large image of the logo on the back of the business card, and the business card details plus a design on the front.

Target Market(s)

High income earners in an affluent Melbourne suburb who value high quality products and done mind paying for it

Industry/Entity Type

Retail

Contact Information for Business Card

Business name: Haddleby's Fine Food Merchant
Address: 27 Quillmont Rd, Tarnvale VIC 3188
Name: TBC
Position Title: Director
Phone Number: TBC
Mobile: TBC

Business name is: Haddleby's Fine Food Merchant. Please allow space for us to fill in the business address, contact number, person's name, position Title and mobile number.

Colors
acd036

Requirements
Must have
• The logo must have our business logo on the back, and our business details and contact details on the front. It must include the colours of white, black and lime green
Nice to have
• It can have different background colours on the front and on the back.
Should not have
• It should not have any other colours aside from white, black and lime green

```html
<!DOCTYPE html>
<html lang="en">
<head>
<meta charset="utf-8">
<title>Haddleby's Fine Food Merchant – Business Card</title>
<link href="https://fonts.googleapis.com/css2?family=Roboto+Slab:wght@400;700&display=swap" rel="stylesheet">
<style>
  :root {
    --lime: #acd036;
    --black: #141414;
    --white: #ffffff;
    --stage: #e9e7e3;
    --ink: #1b1b1b;
    --faint: #f1f2ef;
  }
  * { margin: 0; padding: 0; box-sizing: border-box; }
  html, body { width: 1200px; height: 780px; overflow: hidden; }
  body {
    background: var(--stage);
    font-family: "Roboto Slab", Georgia, serif;
    color: var(--ink);
  }
  .canvas {
    position: relative;
    width: 1200px;
    height: 780px;
  }
  .card {
    position: absolute;
    top: 241px;
    width: 520px;
    height: 298px;
    overflow: hidden;
    box-shadow: 0 6px 18px rgba(0,0,0,0.18);
  }
  /* Back of card */
  .card-back {
    left: 60px;
    background: var(--black);
    display: flex;
    align-items: center;
    justify-content: center;
  }
  .brand-seal {
    display: flex;
    flex-direction: column;
    align-items: center;
    gap: 14px;
  }
  .brand-seal__ring {
    width: 40px;
    height: 40px;
    border: 1.5px solid #6a6a6a;
    border-radius: 50%;
  }
  .brand-seal__name {
    font-weight: 400;
    font-size: 19px;
    letter-spacing: 2px;
    color: #7a7a7a;
    text-align: center;
    max-width: 280px;
    line-height: 1.4;
  }
  /* Front of card */
  .card-front {
    left: 620px;
    background: var(--white);
  }
  .card-front__artwork {
    position: absolute;
    left: 40px;
    top: 14px;
    width: 150px;
    height: 200px;
    border-radius: 40px;
    background: radial-gradient(ellipse at center, #ececea 0%, var(--faint) 60%, var(--white) 100%);
  }
  .person {
    position: absolute;
    left: 250px;
    top: 82px;
    text-align: center;
    width: 200px;
  }
  .person__name {
    font-weight: 700;
    font-size: 15px;
    letter-spacing: 1px;
    text-transform: uppercase;
  }
  .person__role {
    font-size: 12px;
    color: var(--lime);
    margin-top: 1px;
  }
  .contacts {
    position: absolute;
    left: 150px;
    top: 134px;
    width: 330px;
    font-size: 12px;
  }
  .contacts__row {
    display: flex;
    align-items: center;
    gap: 6px;
    margin-bottom: 8px;
  }
  .contacts__divider {
    width: 1px;
    height: 16px;
    background: var(--lime);
    margin: 0 6px;
  }
  .icon { width: 16px; height: 16px; flex: none; }
  .card-front__rule {
    position: absolute;
    left: 0; right: 0;
    top: 210px;
    height: 1px;
    background: var(--black);
  }
  .address-band {
    position: absolute;
    left: 0; right: 0;
    top: 214px;
    height: 46px;
    background: var(--lime);
    display: flex;
    align-items: center;
    justify-content: center;
    font-size: 13px;
    letter-spacing: 0.5px;
    color: var(--ink);
  }
</style>
</head>
<body>
<main class="canvas">

  <section class="card card-back" aria-label="Card back">
    <div class="brand-seal">
      <span class="brand-seal__ring"></span>
      <span class="brand-seal__name">Haddleby's Fine Food Merchant</span>
    </div>
  </section>

  <section class="card card-front" aria-label="Card front">
    <div class="card-front__artwork" role="img" aria-label="Faint line drawing of a vegetable from the brand mark"></div>

    <div class="person">
      <p class="person__name">Colin Ardrey</p>
      <p class="person__role">Founder</p>
    </div>

    <div class="contacts">
      <div class="contacts__row">
        <svg class="icon" viewBox="0 0 16 16" aria-hidden="true">
          <circle cx="8" cy="8" r="7.5" fill="var(--lime)"/>
          <rect x="5.5" y="3.5" width="5" height="9" rx="1" fill="none" stroke="#fff" stroke-width="1.2"/>
          <circle cx="8" cy="10.8" r="0.6" fill="#fff"/>
        </svg>
        <span>(123) 555-0147</span>
        <span class="contacts__divider"></span>
        <svg class="icon" viewBox="0 0 16 16" aria-hidden="true">
          <circle cx="8" cy="8" r="7.5" fill="var(--lime)"/>
          <path d="M4.5 6.5 Q8 3.5 11.5 6.5 L10.5 7.5 L9.5 6.8 L6.5 6.8 L5.5 7.5 Z" fill="#fff"/>
          <rect x="5" y="8" width="6" height="3.5" rx="0.8" fill="#fff"/>
        </svg>
        <span>(123) 555-0147</span>
      </div>
      <div class="contacts__row">
        <svg class="icon" viewBox="0 0 16 16" aria-hidden="true">
          <circle cx="8" cy="8" r="7.5" fill="var(--lime)"/>
          <rect x="4" y="5" width="8" height="6" rx="0.8" fill="#fff"/>
          <path d="M4.3 5.4 L8 8.4 L11.7 5.4" fill="none" stroke="var(--lime)" stroke-width="1"/>
        </svg>
        <span>info@quillmontmail.com</span>
      </div>
    </div>

    <div class="card-front__rule"></div>
    <div class="address-band">27 Quillmont Rd, Tarnvale VIC 3188</div>
  </section>

</main>
</body>
</html>
```